Brantel Construction Core Values Wall Design

Core Values Wall Design for our Wall, I’m not exactly sure visually what we would want it to look like. Maybe some acrylic stand offs that could go on brick? If that’s a possibility. That’s where we have the most space in the office. But we could do other locations too.

These are our core values
• Safety
• Integrity
• Quality
• Client-Focused Solutions
• Continuous Improvement
• Positive Culture and Stewardship

Our vision/mission statement is Steady Craft Built.

```html
<!DOCTYPE html>
<html lang="en">
<head>
<meta charset="utf-8">
<title>Brantel Construction – Core Values Wall</title>
<link rel="stylesheet" href="https://fonts.googleapis.com/css2?family=Montserrat:wght@700&family=Roboto:wght@500&display=swap">
<style>
  :root {
    --panel: #f2efeb;
    --ink: #1d2a44;
    --brand-blue: #1b5c9e;
    --brand-red: #ec2b33;
    --orange: #f7941d;
    --red: #ec3237;
    --navy: #1b5c9e;
    --green: #8dc63f;
    --sky: #29abe2;
    --teal: #14a79d;
    --white: #ffffff;
  }
  html, body {
    margin: 0;
    padding: 0;
    width: 1200px;
    height: 720px;
    overflow: hidden;
    background: var(--panel);
  }
  .values-wall {
    position: relative;
    width: 1200px;
    height: 720px;
    background: var(--panel);
    overflow: hidden;
  }
  .values-art {
    position: absolute;
    inset: 0;
    width: 1200px;
    height: 720px;
  }
  .gear-label {
    font-family: "Roboto", sans-serif;
    font-weight: 500;
    fill: var(--ink);
    text-anchor: middle;
  }
  .gear-label--quality { fill: var(--navy); }
  .company-name {
    font-family: "Montserrat", sans-serif;
    font-weight: 700;
    fill: var(--brand-blue);
    text-anchor: middle;
  }
  .footer-band {
    position: absolute;
    left: 0;
    bottom: 0;
    width: 1200px;
    height: 83px;
    display: flex;
  }
  .footer-band__blue { width: 360px; background: var(--brand-blue); }
  .footer-band__red { flex: 1; background: var(--brand-red); }
  .tagline {
    width: 449px;
    background: var(--white);
    display: flex;
    flex-direction: column;
    align-items: center;
    justify-content: center;
    font-family: "Montserrat", sans-serif;
    font-weight: 700;
    line-height: 1;
  }
  .tagline__main {
    color: var(--brand-blue);
    font-size: 42px;
    letter-spacing: 2px;
  }
  .tagline__sub {
    color: var(--brand-red);
    font-size: 20px;
    letter-spacing: 16px;
    margin-top: 6px;
    padding-left: 16px;
  }
</style>
</head>
<body>
<main class="values-wall">
  <svg class="values-art" viewBox="0 0 1200 720" xmlns="http://www.w3.org/2000/svg">
    <defs>
      <g id="gear-shape">
        <circle r="108" fill="none" stroke="currentColor" stroke-width="28" stroke-dasharray="21.2 21.21"/>
        <circle r="100" fill="currentColor"/>
        <circle r="78" fill="var(--panel)"/>
        <circle r="89" fill="none" stroke="var(--white)" stroke-width="1.6"/>
      </g>
    </defs>

    <g class="gear gear--safety" style="color: var(--orange)" transform="translate(240 180) scale(0.9)">
      <use href="#gear-shape"/>
    </g>
    <text class="gear-label" x="240" y="190" font-size="27">SAFETY</text>

    <g class="gear gear--integrity" style="color: var(--red)" transform="translate(176 353) scale(0.68)">
      <use href="#gear-shape"/>
    </g>
    <text class="gear-label" x="176" y="359" font-size="16">INTEGRITY</text>

    <g class="gear gear--quality" style="color: var(--navy)" transform="translate(331 434) scale(0.62)">
      <use href="#gear-shape"/>
    </g>
    <text class="gear-label gear-label--quality" x="331" y="441" font-size="17">QUALITY</text>

    <g class="gear gear--client" style="color: var(--green)" transform="translate(844 122) scale(0.9)">
      <use href="#gear-shape"/>
    </g>
    <text class="gear-label" x="844" y="100" font-size="16">
      <tspan x="844">CLIENT</tspan>
      <tspan x="844" dy="21">FOCUSED</tspan>
      <tspan x="844" dy="21">SOLUTIONS</tspan>
    </text>

    <g class="gear gear--improvement" style="color: var(--sky)" transform="translate(987 308) scale(1)">
      <use href="#gear-shape"/>
    </g>
    <text class="gear-label" x="987" y="302" font-size="16">
      <tspan x="987">CONTINUOUS</tspan>
      <tspan x="987" dy="22">IMPROVEMENT</tspan>
    </text>

    <g class="gear gear--culture" style="color: var(--teal)" transform="translate(800 462) scale(0.9)">
      <use href="#gear-shape"/>
    </g>
    <text class="gear-label" x="800" y="430" font-size="14">
      <tspan x="800">POSITIVE</tspan>
      <tspan x="800" dy="19">CULTURE</tspan>
      <tspan x="800" dy="19">AND</tspan>
      <tspan x="800" dy="19">STEWARDSHIP</tspan>
    </text>

    <text class="company-name" x="570" y="285" font-size="92">BRANTEL</text>
    <text class="company-name" x="578" y="330" font-size="26" letter-spacing="14">CONSTRUCTION</text>
  </svg>

  <footer class="footer-band">
    <div class="footer-band__blue"></div>
    <div class="tagline">
      <span class="tagline__main">STEADY CRAFT</span>
      <span class="tagline__sub">BUILT</span>
    </div>
    <div class="footer-band__red"></div>
  </footer>
</main>
</body>
</html>
```